Neighbor of existing customer door hanger

We are a landscaping services company (Pest Control & Lawn Fertilization). I am looking for a piece that my sales people can leave behind at the neighbors of our current customers offering our services to them.

I'm not a graphics guy, not even close, I started making a sample that is not any good, but it might give the general idea. I have attached that design here. There is a template available from the printer for 4.25 x 11". I have included that as well

Target Market(s)

Women homeowners 35-50

Industry/Entity Type

Landscape Gardening

Font styles to use
Sans Serif

Colors

Designer to choose colors to be used in the design.

Requirements
Must have
• we are looking for a space to write the name or address of our customer, include 2 specials ( 1 for pest control, 1 for Lawn fertilization and weed control) that make the neighbors feel like they are getting a deal because they are neighbors of our customer.
• the back side of the postcard will list our range of services and have a space for the salesman to write his name.
• This will be printed on a glossy cardstock (unless the designer suggests something else).
• Phone numbers, Website, logos

```html
<!DOCTYPE html>
<html lang="en">
<head>
<meta charset="utf-8">
<title>Verdant Row Door Hanger</title>
<link href="https://fonts.googleapis.com/css2?family=Arimo:ital,wght@0,400;0,700;1,400&display=swap" rel="stylesheet">
<style>
  :root {
    --forest: #0d4d39;
    --leaf: #3f9a2e;
    --leaf-light: #8fd35a;
    --ink: #222222;
    --mist: #c9c9c9;
    --mist-light: #e9e9e9;
    --band: #dfe0e2;
    --meadow: #eef2dc;
    --gold: #e8bd1f;
    --white: #ffffff;
    --page: #efece6;
  }
  * { margin: 0; padding: 0; box-sizing: border-box; }
  html, body { width: 1200px; height: 1000px; overflow: hidden; background: var(--page); }
  body { position: relative; font-family: "Arimo", Arial, sans-serif; color: var(--ink); }

  .door-hanger {
    position: absolute; left: 322px; top: 15px; width: 372px; height: 970px;
    background: var(--white); overflow: hidden;
    box-shadow: 0 4px 14px rgba(0,0,0,.18);
  }
  .abs { position: absolute; }
  .center { left: 0; width: 100%; text-align: center; }

  .hero-photo {
    left: 0; top: 85px; width: 372px; height: 290px;
    background: linear-gradient(160deg, #1f5e1d 0%, #4ea52c 35%, #9bd65a 55%, #3f8e25 75%, #1d5a1c 100%);
  }
  .header { left: 0; top: 0; width: 372px; height: 140px; }
  .brand-name {
    top: 22px; font-size: 28px; font-weight: 700; color: var(--white); letter-spacing: 1px;
  }
  .brand-rule { left: 88px; top: 61px; width: 196px; height: 2px; background: var(--white); }
  .brand-tile {
    top: 72px; width: 44px; height: 44px; border-radius: 5px; background: var(--white);
  }

  .grey-panel { left: 0; top: 330px; width: 372px; height: 256px; }
  .service-icon {
    top: 321px; width: 60px; height: 60px; border-radius: 50%;
    border: 2px solid var(--white);
  }
  .icon-grass { left: 56px; background: linear-gradient(180deg, var(--leaf-light), var(--leaf)); }
  .icon-pest { left: 158px; background: radial-gradient(circle, #ffffff 30%, var(--leaf) 31%); }
  .icon-garden { left: 264px; background: linear-gradient(180deg, #ffffff 50%, #7a5a3a 50%); }

  .greeting { top: 408px; font-size: 30px; font-weight: 700; color: var(--forest); }
  .subhead { top: 455px; font-size: 19px; font-weight: 700; }
  .customer-field {
    left: 46px; top: 489px; width: 280px; height: 39px; border-radius: 12px; background: var(--mist-light);
  }
  .reason { top: 537px; font-size: 16px; font-weight: 700; line-height: 22px; color: #2a2a2a; }

  .heritage-band {
    left: 0; top: 586px; width: 372px; height: 56px; background: var(--band);
    font-size: 16.5px; font-weight: 700; line-height: 22px; padding-top: 6px;
  }

  .meadow {
    left: 0; top: 642px; width: 372px; height: 218px;
    background: linear-gradient(180deg, #d9e4b8 0%, var(--meadow) 40%, #f6f7ee 70%, #e3ecc8 100%);
  }
  .offer-label { top: 654px; font-size: 16px; font-weight: 700; color: var(--forest); }
  .offer-title { top: 677px; font-size: 20px; font-weight: 700; }
  .guarantee {
    left: 130px; top: 718px; width: 242px; height: 34px; background: var(--band);
    font-size: 10px; font-style: italic; padding: 6px 0 0 8px;
    clip-path: polygon(0 0, 100% 0, 100% 100%, 8% 100%);
  }
  .coupon {
    left: 33px; top: 737px; width: 92px; height: 76px; background: var(--gold);
    outline: 2px dashed #333; outline-offset: -3px;
    text-align: center; font-weight: 700;
  }
  .coupon-label { font-size: 11px; margin-top: 12px; }
  .coupon-price { font-size: 19px; line-height: 22px; }
  .coupon-note { font-size: 10px; }
  .lawn-title { left: 196px; top: 761px; font-size: 14px; font-weight: 700; }
  .lawn-note { top: 836px; font-size: 10px; font-weight: 700; }

  .footer {
    left: 0; top: 863px; width: 372px; height: 107px; background: var(--forest);
    color: var(--white); text-align: center; font-weight: 700;
  }
  .phone { font-size: 30px; margin-top: 7px; }
  .website { font-size: 17px; margin-top: 4px; }
</style>
</head>
<body>
  <main class="door-hanger">
    <div class="abs hero-photo" role="img" aria-label="Close-up photo of dewy green grass blades"></div>

    <svg class="abs header" viewBox="0 0 372 140" aria-hidden="true">
      <path d="M0 0 H372 V112 Q340 92 260 118 Q186 140 112 118 Q32 92 0 112 Z" fill="var(--forest)"/>
    </svg>
    <div class="abs center brand-name">Verdant Row</div>
    <div class="abs brand-rule"></div>
    <div class="abs brand-tile" style="left:108px" role="img" aria-label="Lawn care icon"></div>
    <div class="abs brand-tile" style="left:164px" role="img" aria-label="Pest control icon"></div>
    <div class="abs brand-tile" style="left:220px" role="img" aria-label="Landscaping icon"></div>

    <svg class="abs grey-panel" viewBox="0 0 372 256" aria-hidden="true">
      <defs>
        <linearGradient id="greyFade" x1="0" y1="0" x2="0" y2="1">
          <stop offset="0" stop-color="#d4d4d4"/>
          <stop offset="0.5" stop-color="#bdbdbd"/>
          <stop offset="1" stop-color="#a8a8a8"/>
        </linearGradient>
      </defs>
      <path d="M0 10 Q186 -14 372 10 V256 H0 Z" fill="var(--forest)"/>
      <path d="M0 52 Q60 30 186 32 Q312 30 372 52 V256 H0 Z" fill="url(#greyFade)"/>
    </svg>
    <div class="abs service-icon icon-grass" role="img" aria-label="Grass icon"></div>
    <div class="abs service-icon icon-pest" role="img" aria-label="Spider icon"></div>
    <div class="abs service-icon icon-garden" role="img" aria-label="Garden shovel icon"></div>

    <h1 class="abs center greeting">Hey Neighbor !</h1>
    <p class="abs center subhead">We service your Friends</p>
    <div class="abs customer-field" aria-label="Space for customer name or address"></div>
    <p class="abs center reason">Because your friends use our services,<br>You get Neighborhood discounts!</p>

    <p class="abs center heritage-band">Family owned &amp; operated in<br>Salt Lake City for over 25 years!</p>

    <div class="abs meadow" role="img" aria-label="Soft-focus photo of a sunlit lawn"></div>
    <p class="abs center offer-label">Neighborhood Discounts on:</p>
    <h2 class="abs center offer-title">Full Servvice Pest Control</h2>
    <p class="abs guarantee">“You won’t see a bug or we re-treat for Free”</p>
    <div class="abs coupon">
      <p class="coupon-label">Your cost</p>
      <p class="coupon-price">$9.95</p>
      <p class="coupon-note">First Service</p>
    </div>
    <h2 class="abs lawn-title">Lawn Fertilization</h2>
    <p class="abs center lawn-note">Thick Green Grass &amp; No Weeds</p>

    <footer class="abs footer">
      <p class="phone">555-014-2290</p>
      <p class="website">www.GETVERDANTROW.com</p>
    </footer>
  </main>
</body>
</html>
```